Business Card Design for a Software Startup

We'd like to have a business card design. We already have a logo. Basically what we need is a clean design with name, address, cellphone and phone numbers, e-mail and web site address (front) and a space on the back with our logo with the company name on the right side and some texts on the bottom.
We are a development and consulting company in Brazil with highly qualified team of professionals in Java, iOS and Android development and consulting.

Target Market(s)

CIO, IT managers of mid to big size companies

Industry/Entity Type

Business

```html
<!DOCTYPE html>
<html lang="en">
<head>
<meta charset="utf-8">
<title>VOLTRA – Business Card</title>
<link rel="stylesheet" href="https://fonts.googleapis.com/css2?family=Mulish:wght@400;700;800&display=swap">
<style>
  :root {
    --bg: #1c2230;
    --paper: #f7f7f5;
    --navy: #1d3a6b;
    --navy-deep: #173260;
    --navy-ink: #1b2d52;
    --sky: #1f86c9;
    --frame-light: #d5d7da;
    --text-grey: #2f3a4c;
    --frame-dark: #2d4f86;
  }
  * { margin: 0; padding: 0; box-sizing: border-box; }
  html, body {
    width: 1200px; height: 800px; overflow: hidden;
    background: var(--bg);
    font-family: "Mulish", sans-serif;
  }
  .canvas { position: relative; width: 1200px; height: 800px; }

  .card {
    position: absolute; top: 245px;
    width: 540px; height: 310px;
    border-radius: 6px; overflow: hidden;
  }
  .card-front { left: 45px; background: var(--paper); }
  .card-back  { left: 615px; background: var(--navy-deep); }
  .card-art { position: absolute; inset: 0; }

  .wordmark {
    position: absolute; display: flex; align-items: center; gap: 12px;
    font-weight: 800; letter-spacing: 0.5px; line-height: 1;
  }
  .wordmark-square { width: 44px; height: 44px; border-radius: 5px; }
  .card-front .wordmark { left: 48px; top: 58px; font-size: 50px; color: var(--navy-ink); }
  .card-front .wordmark-square { background: var(--sky); }
  .card-back .wordmark { left: 50%; top: 50%; transform: translate(-50%, -50%); font-size: 58px; color: #ffffff; }
  .card-back .wordmark-square { width: 52px; height: 52px; background: #ffffff; }

  .person {
    position: absolute; right: 60px; top: 140px; text-align: right;
  }
  .person-name { font-weight: 800; font-size: 17px; color: var(--navy-ink); letter-spacing: 0.5px; }
  .person-role { font-size: 13px; color: var(--sky); margin-top: 2px; }

  .contact {
    position: absolute; bottom: 56px; left: 0; right: 60px;
    display: flex; justify-content: flex-end; align-items: flex-end; gap: 16px;
    font-size: 12.5px; color: var(--text-grey);
  }
  .address { text-align: right; line-height: 1.6; }
  .divider { width: 1px; height: 40px; background: var(--text-grey); }
  .channels { line-height: 1.6; }
  .channel { display: flex; align-items: center; gap: 8px; }
  .channel svg { width: 12px; height: 12px; flex: none; }
</style>
</head>
<body>
<main class="canvas">

  <section class="card card-front">
    <svg class="card-art" viewBox="0 0 540 310" aria-hidden="true">
      <path d="M150 282 H470 Q495 282 500 262 L507 250 V280 Q505 296 485 296 H150 Z" fill="var(--sky)"/>
      <path d="M42 18 H470 L518 58 V258 Q518 278 498 278 H70 L22 240 V38 Q22 18 42 18 Z"
            fill="none" stroke="var(--frame-light)" stroke-width="1.5"/>
    </svg>

    <div class="wordmark"><span class="wordmark-square"></span>VOLTRA</div>

    <div class="person">
      <p class="person-name">LUCAS MOREIRA</p>
      <p class="person-role">Managing director</p>
    </div>

    <div class="contact">
      <p class="address">Av. Paulo Andrade 418<br>9o andar - Centro</p>
      <span class="divider"></span>
      <div class="channels">
        <p class="channel">
          <svg viewBox="0 0 12 12"><rect x="1" y="1" width="10" height="10" rx="1.5" fill="var(--sky)"/><rect x="3" y="3" width="2" height="6" fill="#fff"/><rect x="6" y="3" width="3" height="2" fill="#fff"/></svg>
          +55-61-200345512
        </p>
        <p class="channel">
          <svg viewBox="0 0 12 12"><rect x="0.5" y="2" width="11" height="8" rx="1" fill="var(--sky)"/><path d="M1 3 L6 7 L11 3" fill="none" stroke="#fff" stroke-width="1"/></svg>
          info@voltra.com
        </p>
      </div>
    </div>
  </section>

  <section class="card card-back">
    <svg class="card-art" viewBox="0 0 540 310" aria-hidden="true">
      <path d="M42 18 H470 L518 58 V258 Q518 278 498 278 H70 L22 240 V38 Q22 18 42 18 Z"
            fill="#1f3f74" stroke="var(--frame-dark)" stroke-width="2"/>
      <path d="M150 292 H485 Q505 292 510 272 V120" fill="none" stroke="var(--sky)" stroke-width="3"/>
    </svg>
    <div class="wordmark"><span class="wordmark-square"></span>VOLTRA</div>
  </section>

</main>
</body>
</html>
```